Marlowe Holdings LLC - Business Cards

Need the following information on the cards:

Name: Dean R Vossler
Title: Chief Executive Manager

Business address:
412 N Ridgeview Lane #118
Harlow Springs, NV 60412

Phone: (775) 555-0148 - Business
KPV FFL license number: 5-21-xxx-xx-xx-04519
Email: dean.vossler@marloweholdingsffl.com

Target Market(s)

Firearm owners

Industry/Entity Type

Firearms industry,

Contact Information for Business Card

Contact number, name and title, web page address, email, business address and kpv license number,

Requirements
Must have
• Name, title, business address, phone numbers, KPV license numbers, web page address and email address.
Nice to have
• Cellphone number,

```html
<!DOCTYPE html>
<html lang="en">
<head>
<meta charset="utf-8">
<title>Marlowe Holdings LLC – Business Cards</title>
<link href="https://fonts.googleapis.com/css2?family=Arimo:wght@400;700&display=swap" rel="stylesheet">
<style>
  :root {
    --brand-red: #e93137;
    --charcoal: #383536;
    --stage: #e6e7e9;
    --paper: #ffffff;
    --ink: #2e2c2d;
    --map-tone: #eceded;
  }
  * { box-sizing: border-box; margin: 0; padding: 0; }
  html, body {
    width: 1200px; height: 729px; overflow: hidden;
    background: var(--stage);
    font-family: "Arimo", Arial, sans-serif;
  }
  .stage { position: relative; width: 1200px; height: 729px; }

  .card {
    position: absolute; top: 186px;
    width: 507px; height: 296px;
    background: var(--paper); overflow: hidden;
  }
  .card--back { left: 65px; }
  .card--front { left: 628px; }

  .back-panel { position: absolute; inset: 0; }

  .holder-name {
    position: absolute; left: 15px; top: 52px;
    color: #fff; font-weight: 700; font-size: 24px; line-height: 1;
  }
  .holder-title {
    position: absolute; left: 15px; top: 78px;
    color: #fff; font-size: 11px; line-height: 1;
  }

  .contact-icon {
    position: absolute; left: 9px; width: 26px; height: 26px;
  }
  .contact-text {
    position: absolute; left: 45px;
    color: #fff; font-size: 11px; line-height: 12.8px; white-space: nowrap;
  }

  .logo-spot {
    position: absolute; left: 344px; top: 77px; width: 112px; height: 112px;
    display: flex; align-items: center; justify-content: center;
  }
  .logo-ring {
    position: absolute; width: 108px; height: 108px; border-radius: 50%;
    border: 1.5px solid var(--charcoal);
  }
  .logo-name {
    position: relative; text-align: center;
    color: var(--brand-red); font-weight: 700; font-size: 15px; line-height: 1.1;
  }

  .back-company {
    position: absolute; left: 318px; width: 160px; top: 198px;
    text-align: center; color: var(--ink);
    font-weight: 700; font-size: 14.6px; line-height: 16.2px;
  }

  .world-map {
    position: absolute; left: 56px; top: 50px; width: 395px; height: 195px;
    border-radius: 50%;
    background: radial-gradient(ellipse at center, var(--map-tone) 0%, rgba(236,237,237,0.7) 50%, rgba(255,255,255,0) 72%);
  }
  .front-logo {
    position: absolute; left: 209px; top: 40px; width: 90px; height: 88px;
    display: flex; align-items: center; justify-content: center;
  }
  .front-logo .logo-ring { width: 84px; height: 84px; }
  .front-logo .logo-name { font-size: 11.5px; }

  .front-company {
    position: absolute; left: 0; right: 0; top: 146px; text-align: center;
    color: var(--ink); font-weight: 700; font-size: 17.5px; line-height: 1;
  }
  .front-url {
    position: absolute; left: 0; right: 0; top: 238px; text-align: center;
    color: var(--brand-red); font-weight: 700; font-size: 15px; line-height: 1;
  }

  .side-label {
    position: absolute; top: 524px; width: 200px; text-align: center;
    color: var(--ink); font-size: 24px; line-height: 1;
  }
  .side-label--back { left: 225px; }
  .side-label--front { left: 789px; }

  .palette { position: absolute; left: 552px; top: 560px; display: flex; height: 19px; }
  .palette__chip { width: 59px; height: 19px; }
  .palette__chip--red { background: var(--brand-red); }
  .palette__chip--dark { background: var(--charcoal); }
</style>
</head>
<body>
<main class="stage">

  <section class="card card--back" aria-label="Card back">
    <svg class="back-panel" viewBox="0 0 507 296" width="507" height="296" aria-hidden="true">
      <path d="M0 0 H240 Q354 148 240 296 H0 Z" fill="var(--brand-red)"/>
      <path d="M0 0 H220 Q346 150 230 296 H0 Z" fill="var(--charcoal)"/>
    </svg>

    <h1 class="holder-name">Dean R Vossler</h1>
    <p class="holder-title">Chief Executive Manager</p>

    <svg class="contact-icon" style="top:147px" viewBox="0 0 26 26" aria-hidden="true">
      <circle cx="13" cy="13" r="13" fill="var(--brand-red)"/>
      <path d="M9.2 6.5c.6-.4 1.3-.2 1.6.4l1.3 2.4c.3.6.1 1.2-.4 1.5l-.9.6c.5 1.6 1.6 3 3 3.8l.7-.8c.4-.5 1.1-.6 1.6-.2l2.2 1.6c.5.4.6 1.1.2 1.6l-1 1.2c-.6.7-1.6.9-2.5.6-3.7-1.4-6.4-4.6-7.2-8.5-.2-.9.2-1.8 1-2.3z" fill="#fff"/>
    </svg>
    <p class="contact-text" style="top:154px">(775) 555-0148 - Business</p>

    <svg class="contact-icon" style="top:179px" viewBox="0 0 26 26" aria-hidden="true">
      <circle cx="13" cy="13" r="13" fill="var(--brand-red)"/>
      <path d="M6.5 8.5 L20 12.5 L6.5 17 L9.5 12.8 Z" fill="#fff"/>
      <path d="M11 14.5 L12.5 19.5 L14 15" fill="#fff"/>
    </svg>
    <p class="contact-text" style="top:180px">dean.vossler@marloweholdingsffl.com<br>KPV FFL license number: 5-21-xxx-xx-xx-04519</p>

    <svg class="contact-icon" style="top:212px" viewBox="0 0 26 26" aria-hidden="true">
      <circle cx="13" cy="13" r="13" fill="var(--brand-red)"/>
      <path d="M6 13 L13 6.8 L20 13" fill="none" stroke="#fff" stroke-width="2" stroke-linejoin="round"/>
      <path d="M8.5 12.8 V19 H11.8 V15.5 H14.2 V19 H17.5 V12.8 L13 9 Z" fill="#fff"/>
    </svg>
    <p class="contact-text" style="top:212px">412 N Ridgeview Lane #118<br>Harlow Springs, NV 60412</p>

    <div class="logo-spot">
      <span class="logo-ring" aria-hidden="true"></span>
      <span class="logo-name">MARLOWE<br>HOLDINGS</span>
    </div>
    <p class="back-company">MARLOWE<br>HOLDINGS LLC</p>
  </section>

  <section class="card card--front" aria-label="Card front">
    <div class="world-map" role="img" aria-label="Faint world map backdrop"></div>
    <div class="front-logo">
      <span class="logo-ring" aria-hidden="true"></span>
      <span class="logo-name">MARLOWE<br>HOLDINGS</span>
    </div>
    <p class="front-company">MARLOWE HOLDINGS LLC</p>
    <p class="front-url">www.marloweholdingsffl.com</p>
  </section>

  <p class="side-label side-label--back">BACK</p>
  <p class="side-label side-label--front">FRONT</p>

  <div class="palette" aria-label="Colour palette">
    <span class="palette__chip palette__chip--red"></span>
    <span class="palette__chip palette__chip--dark"></span>
  </div>
</main>
</body>
</html>
```